Design a Bold Tradeshow Backdrop for a Sustainable Cleaning Technology

We need a professional, high-impact 10' × 8' tradeshow backdrop for Vornelle®, a commercial cleaning technology company. 143.75" x 90" high and needs bleeds in the 143.75" direction for printing but the graphic area is 10' wide.

Our first event will have an audience that includes K–12 school administrators, facility managers, business officials, and custodial decision-makers. However, this backdrop will be used at multiple future trade shows across different commercial and institutional markets.

The design therefore needs to be universal rather than specifically education- or school-themed.

Our goal is to stop attendees as they walk past the booth and immediately communicate a simple message:

Safer and more sustainable cleaning can also cost substantially less than conventional cleaning chemicals.

We want the design to feel modern, innovative, clean, sustainable, credible, commercial, and premium. It should resonate with K–12 decision-makers while being equally appropriate at events serving commercial facilities, healthcare, hospitality, government, property management, transportation, and other institutional markets.

It should NOT look like a traditional janitorial supply advertisement and should not be overly busy.

The most important messages need to be understandable from approximately 10–20 feet away.

Required Messaging

The primary headline should be:

SUSTAINABLE CLEANING
DOES NOT HAVE TO BE EXPENSIVE.

Three major value propositions should be prominently displayed:

FREE
Cleaning Chemical Analysis
See how much you can save.

SAVE UP TO 60% or More
on Cleaning Chemical Costs

AS LITTLE AS $0.27/GALLON

We would also like a strong secondary message incorporated into the design:

SMARTER CLEANING.
High Performance. Low Cost. Safer.

Visual Direction — Important

Rather than showing a K–12 school hallway or other environment that limits the backdrop to the education market, we want a sophisticated, universal commercial or institutional environment.

This could be a bright, contemporary commercial facility, lobby, corridor, office environment, public building, or other premium architectural space that could reasonably represent many different types of facilities.

The environment should communicate:

Cleanliness • Safety • Sustainability • Professionalism • Efficiency • High Performance

We want someone from a school, hospital, hotel, office building, airport, government facility, or other commercial property to be able to look at the backdrop and relate the imagery to their own facility.

Please avoid imagery that makes the backdrop industry-specific.

We also want to avoid clichéd environmental imagery. The design does not need to be covered in leaves, trees, water droplets, recycling symbols, or other obvious "green" graphics to communicate sustainability. We prefer a sophisticated commercial interpretation of sustainability.

Color & Brand Direction

We want the overall color palette to stay primarily within:

Blues — consistent with our corporate identity

Greens — to reinforce sustainability, safety, efficiency, and environmental responsibility

White — strongly encouraged for clean space, contrast, and an open contemporary appearance

Black — should be limited primarily to text where necessary for readability

Please avoid making black a major background or dominant design color.

We want the finished display to have a bright, clean, sophisticated, sustainable look and feel rather than a dark or industrial appearance.

The design should use significant negative space and a strong visual hierarchy.

Less is more.

We prefer a few large, powerful messages that can be understood quickly rather than numerous small bullet points, paragraphs, or icons.

Creative Freedom

The attached concept image is provided to communicate our general direction and messaging only.

It does not need to be copied.

We are specifically running this contest because we want designers to improve upon our initial concept and show us different creative approaches to presenting the Vornelle value proposition.

We are open to creative interpretations of the commercial environment, composition, typography, use of negative space, and how the three major financial benefits are presented.

The finished design should feel like an innovative commercial technology brand, not simply another cleaning chemical company.

Corporate Logo — Very Important

We are attaching our official Vornelle® corporate logo for use in the design.

DO NOT redraw, recreate, modify, stylize, reinterpret, trace, or AI-generate the Vornelle logo.

The supplied corporate logo must be inserted directly into the artwork exactly as provided, maintaining its original proportions, colors, typography, trademark elements, and graphic design.

The logo should generally appear in the upper-left area of the backdrop but should not overwhelm the primary marketing message.

Printer Template & Graphic Sizing

We are also attaching the printer's official graphic template and instructions for the 8' × 8' tension-fabric display.

Designers should create their artwork using these supplied specifications so the winning design can be transferred directly into production.

The printer requires that the original document size not be changed, artwork be created on the designated design layer or a new layer, images be embedded, text be converted to outlines, and the finished production artwork be supplied as a PDF.

Please pay particular attention to the bleed area, finished size, and safe artwork area when positioning important text, graphics, and the corporate logo.

Physical Booth Context

The backdrop will sit behind an 8' tradeshow table.

The complete booth will also contain:

A blue stretch tablecloth with the Vornelle corporate logo
BrevoMax and Vornelle product containers and samples on the table
An HulaDrent chemical mixing/dilution station displayed on an elevated stand to the left
A television/monitor to the right demonstrating our online ROI cost-savings calculator

Because these other booth elements will explain our products and technology in greater detail, the backdrop should NOT attempt to explain everything we do.

Its primary purpose is to stop traffic, establish the Vornelle brand, and communicate our core economic and sustainability value proposition.

Final Deliverables

The winning designer must provide artwork properly sized and positioned using our supplied 8' × 8' tension-fabric display template.

Final files should include:

Print-ready, high-resolution PDF
Editable source/vector artwork
All images embedded
Fonts converted to outlines
Artwork correctly positioned within the supplied printer template
Original Vornelle corporate logo incorporated without modification
The 3–5 Second Test

This is perhaps the most important requirement.

Someone walking down a tradeshow aisle should be able to look at the backdrop for 3–5 seconds and understand:

Vornelle offers safer, sustainable, high-performance commercial cleaning — at a lower cost.

The three offers we particularly want them to remember are:

FREE CHEMICAL ANALYSIS

SAVE UP TO 60%

AS LITTLE AS $0.27/GALLON

The overall takeaway should be:

Sustainable cleaning does not have to cost more.

We want the winning design to make that message immediately understandable, credible, and memorable.

Colors
0054AA
0677BA
7BADD7
CADEEF
E8F1F8
0094D4
00A9DD
6FCCEA
C7EBF8
E9F6FB
00AB8E
00BBA5
67D7C9
C6EFE9
E9F9F6
59FF00
82FF00
B8FF75
E3FFCB
F4FFEA

```html
<!DOCTYPE html>
<html lang="en">
<head>
<meta charset="utf-8">
<title>Vornelle Tradeshow Backdrop</title>
<link href="https://fonts.googleapis.com/css2?family=Outfit:wght@300;400;600;700;800&family=Hind:wght@600;700&display=swap" rel="stylesheet">
<style>
  :root {
    --brand-blue: #0054AA;
    --column-blue: #0677BA;
    --column-blue-deep: #0a6bb3;
    --icon-gold: #F0B400;
    --panel-white: #ffffff;
    --stage-grey: #f2f4f6;
    --suit-light: #e9edf1;
    --suit-shade: #cfd6dd;
    --table-dark: #3a2a22;
    --table-mid: #5a3f30;
  }
  * { margin: 0; padding: 0; box-sizing: border-box; }
  html, body { width: 1200px; height: 1121px; overflow: hidden; background: var(--stage-grey); }
  .backdrop {
    position: relative; width: 1200px; height: 1121px;
    background: var(--panel-white); overflow: hidden;
    font-family: "Outfit", sans-serif; color: var(--brand-blue);
  }
  .price-column {
    position: absolute; left: 650px; top: 0; width: 432px; height: 1080px;
    background: linear-gradient(180deg, var(--column-blue-deep), var(--column-blue));
  }
  .photo-worker {
    position: absolute; left: 600px; top: 20px; width: 530px; height: 470px;
    background: radial-gradient(ellipse at 55% 45%, var(--suit-light) 0%, var(--suit-shade) 70%, rgba(207,214,221,0) 100%);
  }
  .photo-table {
    position: absolute; left: 650px; top: 490px; width: 550px; height: 205px;
    background: linear-gradient(160deg, var(--table-mid), var(--table-dark));
  }
  .brand {
    position: absolute; left: 75px; top: 148px;
    font-family: "Outfit", sans-serif; font-weight: 600; font-size: 60px;
    color: var(--brand-blue); letter-spacing: -0.5px; line-height: 1;
  }
  .headline { position: absolute; left: 75px; top: 350px; }
  .headline-lead { font-weight: 400; font-size: 34px; letter-spacing: 0.5px; line-height: 1.2; }
  .headline-main { font-weight: 700; font-size: 54px; line-height: 1.25; letter-spacing: 0.3px; }
  .offer { position: absolute; left: 75px; display: flex; gap: 26px; }
  .offer-first { top: 600px; }
  .offer-second { top: 750px; }
  .offer-icon {
    width: 58px; height: 62px; border: 4px solid var(--icon-gold);
    display: flex; align-items: center; justify-content: center; flex-shrink: 0; margin-top: 2px;
  }
  .offer-text {
    font-family: "Hind", sans-serif; font-weight: 700; font-size: 26px;
    line-height: 1.35; width: 400px; letter-spacing: -0.4px;
  }
  .tagline {
    position: absolute; left: 75px; top: 985px;
    font-weight: 300; font-style: italic; font-size: 26px; line-height: 1.3;
  }
  .price {
    position: absolute; left: 650px; top: 740px; width: 432px; text-align: center;
    color: var(--panel-white); font-weight: 700;
  }
  .price-lead { font-size: 52px; line-height: 1; }
  .price-amount { font-size: 150px; font-weight: 800; line-height: 1; letter-spacing: -3px; margin-top: 8px; }
  .price-unit { font-size: 56px; line-height: 1; margin-top: 8px; }
</style>
</head>
<body>
<main class="backdrop">
  <div class="price-column"></div>
  <div class="photo-worker" role="img" aria-label="Cleaning technician in white protective suit, goggles and mask, spraying a surface"></div>
  <div class="photo-table" role="img" aria-label="Dark wooden tabletop being wiped with a cloth"></div>

  <p class="brand">Vornelle®</p>

  <h1 class="headline">
    <span class="headline-lead">SUSTAINABLE CLEANING</span><br>
    <span class="headline-main">DOES NOT HAVE<br>TO BE EXPENSIVE</span>
  </h1>

  <div class="offer offer-first">
    <div class="offer-icon">
      <svg width="34" height="40" viewBox="0 0 34 40" fill="none" stroke="#0054AA" stroke-width="4" stroke-linejoin="round">
        <line x1="8" y1="3" x2="26" y2="3"/>
        <path d="M12 3 V15 L4 36 H30 L22 15 V3"/>
        <line x1="9" y1="26" x2="25" y2="26"/>
      </svg>
    </div>
    <p class="offer-text">FREE CLEANING CHEMICAL<br>ANALYSIS - SEE HOW MUCH<br>YOU CAN SAVE.</p>
  </div>

  <div class="offer offer-second">
    <div class="offer-icon">
      <svg width="46" height="44" viewBox="0 0 46 44" fill="none">
        <text x="2" y="36" font-family="Outfit, sans-serif" font-size="36" font-weight="400" fill="#0054AA">$</text>
        <path d="M24 20 L30 27 L42 12" stroke="#0054AA" stroke-width="4" stroke-linecap="round" stroke-linejoin="round"/>
      </svg>
    </div>
    <p class="offer-text">SAVE UP TO 60% OR MORE<br>ON CLEANING CHEMICAL<br>COSTS</p>
  </div>

  <p class="tagline">SMARTER CLEANING.<br>HIGH PERFORMANCE.<br>LOW COST. SAFER.</p>

  <div class="price">
    <p class="price-lead">AS LITTLE AS</p>
    <p class="price-amount">$0.27</p>
    <p class="price-unit">/GALLON</p>
  </div>
</main>
</body>
</html>
```